Pamphlet for introducing people to our church

I would like a church pamphlet designed, that includes the content in file "tovik-pamphlet.txt".

I am looking for a design that will incorporate the content in a professional and creative manner.

You do not have to use the content in any specific order, but I am relying on your skill and design knowledge to organize everything in an artistic and effective way.

Target Market(s)

Everyone

Industry/Entity Type

Religious

Requirements
Must have
• logo, use of content provided, use of branding (logo colors)
Nice to have
• More images where necessary
Should not have
• cross

```html
<!DOCTYPE html>
<html lang="en">
<head>
<meta charset="utf-8">
<title>Tovik — Church Pamphlet</title>
<link rel="stylesheet" href="https://fonts.googleapis.com/css2?family=Raleway:ital,wght@0,300;0,400;0,500;0,600;0,700;0,800;1,500&display=swap">
<style>
  :root {
    --navy: #0f2d57;
    --navy-deep: #0a2248;
    --blue: #1f5ea8;
    --blue-bright: #2f7fd0;
    --orange: #f39200;
    --orange-soft: #f7b54a;
    --ink: #203450;
    --paper: #ffffff;
    --mist: #eef1f5;
  }
  * { box-sizing: border-box; margin: 0; padding: 0; }
  html, body { width: 1200px; height: 854px; overflow: hidden; background: #dcdcdc; }
  body { font-family: "Raleway", sans-serif; }
  .pamphlet { position: relative; width: 1200px; height: 854px; background: var(--paper); overflow: hidden; }

  /* Left panel */
  .panel-left {
    position: absolute; left: 0; top: 0; width: 405px; height: 854px;
    background: linear-gradient(160deg, #14406f 0%, var(--navy) 45%, var(--navy-deep) 100%);
    color: #fff;
  }
  .panel-left .texture { position: absolute; inset: 0; }
  .mission { position: absolute; left: 50px; top: 232px; width: 335px; }
  .mission-title { line-height: 1; }
  .mission-title .kicker { display: block; color: var(--orange); font-weight: 800; font-size: 26px; letter-spacing: .5px; }
  .mission-title .rest { display: block; color: #fff; font-weight: 300; font-size: 27px; letter-spacing: .5px; margin-top: 1px; }
  .mission-body { position: absolute; left: 50px; top: 307px; width: 340px; font-size: 11.2px; line-height: 1.42; font-weight: 500; }
  .mission-body p + p { margin-top: 15px; }
  .mission-rule { position: absolute; left: 36px; top: 304px; width: 6px; height: 248px; background: var(--orange); }
  .brand { position: absolute; left: 38px; top: 742px; color: #fff; }
  .brand-row { display: flex; align-items: center; gap: 8px; }
  .brand-dot { width: 12px; height: 12px; border-radius: 50%; background: var(--orange); }
  .brand-name { font-size: 30px; font-weight: 500; letter-spacing: 1px; }
  .brand-tag { font-size: 7px; font-weight: 500; letter-spacing: .6px; margin-top: 2px; color: #fff; }

  /* Right panel */
  .decor { position: absolute; left: 405px; top: 0; width: 795px; height: 660px; }
  .ministries { position: absolute; left: 450px; top: 256px; width: 320px; }
  .ministries h2 { color: var(--navy); font-size: 27px; font-weight: 800; letter-spacing: .5px; }
  .ministry { position: absolute; left: 0; display: flex; gap: 11px; width: 330px; }
  .ministry-photo { flex: none; width: 57px; height: 57px; border-radius: 50%; }
  .ministry h3 { color: var(--orange); font-size: 17px; font-weight: 800; line-height: 1.1; }
  .ministry .sub { color: var(--orange); font-size: 11px; font-style: italic; font-weight: 500; }
  .ministry p { color: var(--ink); font-size: 12px; line-height: 1.35; margin-top: 3px; }

  .service { position: absolute; left: 836px; top: 323px; width: 340px; color: var(--navy); }
  .service .time { font-size: 15px; font-weight: 800; }
  .service address { font-style: normal; font-size: 17.5px; line-height: 1.3; margin-top: 2px; }
  .service .web { font-size: 16px; font-weight: 700; font-style: italic; margin-top: 12px; }
  .service .help { font-size: 12.5px; font-weight: 800; line-height: 1.3; margin-top: 18px; }
  .service .help span { color: var(--orange); }

  /* Photo strip */
  .strip-bar-orange { position: absolute; left: 405px; top: 657px; width: 395px; height: 12px; background: var(--orange); }
  .strip-bar-navy { position: absolute; left: 800px; top: 657px; width: 400px; height: 12px; background: var(--navy); }
  .tile { position: absolute; top: 669px; height: 185px; }
</style>
</head>
<body>
<div class="pamphlet">

  <section class="panel-left">
    <svg class="texture" width="405" height="854" role="img" aria-label="Faint blue triangle texture">
      <defs>
        <linearGradient id="sheen" x1="0" y1="0" x2="1" y2="1">
          <stop offset="0" stop-color="#2a67aa" stop-opacity=".35"/>
          <stop offset="1" stop-color="#0a2248" stop-opacity="0"/>
        </linearGradient>
      </defs>
      <rect width="405" height="854" fill="url(#sheen)"/>
    </svg>

    <h1 class="mission mission-title"><span class="kicker">MISSION</span><span class="rest">STATEMENT:</span></h1>
    <div class="mission-rule"></div>
    <div class="mission-body">
      <p>TOVIK is a gathering of believers whose purpose is to seek the face of God for an authentic restoration of the church as a body of born again believers around the world. As a gathering of believers, TOVIK seeks an awakening of the mind founded on the precepts and teachings of Jesus Christ.</p>
      <p>The modern church has replaced the simple and Kingdom centered principles of Jesus's disciples with complacent and compromised teachings on earthly prosperity. We believe in humbly seeking God without motive to use God or His Word for our own gain. The end times church will experience a glorious revival, renewed love and zeal for true discipleship, faith, and godliness as Jesus intended for us.</p>
    </div>

    <div class="brand">
      <div class="brand-row"><span class="brand-dot"></span><span class="brand-name">TOVIK</span></div>
      <div class="brand-tag">A VOICE TO ALL NATIONS</div>
    </div>
  </section>

  <svg class="decor" width="795" height="660" role="img" aria-label="Faceted blue and orange geometric decoration">
    <defs>
      <linearGradient id="facet" x1="0" y1="0" x2="1" y2="1">
        <stop offset="0" stop-color="#1f5ea8"/>
        <stop offset=".55" stop-color="#2f7fd0"/>
        <stop offset=".8" stop-color="#f39200"/>
        <stop offset="1" stop-color="#f7c200"/>
      </linearGradient>
      <linearGradient id="wash" x1="0" y1="0" x2="1" y2="0">
        <stop offset="0" stop-color="#eef1f5" stop-opacity=".8"/>
        <stop offset="1" stop-color="#ffffff" stop-opacity="0"/>
      </linearGradient>
    </defs>
    <rect width="795" height="660" fill="url(#wash)"/>
    <polygon points="560,0 795,0 795,410 735,250 620,90" fill="url(#facet)" opacity=".95"/>
  </svg>

  <section class="ministries">
    <h2>MINISTRIES:</h2>
    <div class="ministry" style="top:56px">
      <div class="ministry-photo" role="img" aria-label="Photo of a child in prayer" style="background:radial-gradient(circle,#8a6a55,#2b2320)"></div>
      <div>
        <h3>Kingdom seeds</h3>
        <div class="sub">(Children's ministry)</div>
        <p>Children learn to be seeds of godliness<br>in the world.</p>
      </div>
    </div>
    <div class="ministry" style="top:145px">
      <div class="ministry-photo" role="img" aria-label="Photo of a person with raised arms at sunset" style="background:radial-gradient(circle at 50% 40%,#f3c98a,#6a89b0)"></div>
      <div>
        <h3>School of pilgrims</h3>
        <p>Learn the basics of Christian faith and<br>about God's purpose for your life.</p>
      </div>
    </div>
    <div class="ministry" style="top:212px">
      <div class="ministry-photo" role="img" aria-label="Photo of hands holding a young plant" style="background:radial-gradient(circle,#9bb56a,#3f5a2e)"></div>
      <div>
        <h3>School of disciples</h3>
        <p>Deepen your knowledge of God's word<br>and learn how to server him.</p>
      </div>
    </div>
  </section>

  <section class="service">
    <div class="time">Sunday Service: 10:00am-12:30pm</div>
    <address>Linden Community Center<br>48 Harbor Lane<br>Fairview, ME 04010</address>
    <div class="web">Visit us at www.tovik.org</div>
    <div class="help">If you need prayer or counseling give us a call at <span>+1 555-014-2273</span> or email us at <span>contact@cedarhillfellowship.org</span></div>
  </section>

  <div class="strip-bar-orange"></div>
  <div class="strip-bar-navy"></div>
  <div class="tile" role="img" aria-label="Photo of hands folded over an open book" style="left:405px;width:125px;background:linear-gradient(160deg,#d8d8d8,#6b6b6b)"></div>
  <div class="tile" style="left:530px;width:215px;background:linear-gradient(180deg,#1a3f6e,#0f2d57)"></div>
  <div class="tile" role="img" aria-label="Photo of an elderly person praying" style="left:745px;width:135px;background:linear-gradient(160deg,#bdbdbd,#4c4c4c)"></div>
  <div class="tile" style="left:880px;width:80px;background:var(--orange)"></div>
  <div class="tile" role="img" aria-label="Photo of a person kneeling in light" style="left:960px;width:95px;background:linear-gradient(160deg,#f2f2f2,#9a9a9a)"></div>
  <div class="tile" role="img" aria-label="Photo of a silhouette on a hill" style="left:1055px;width:145px;background:linear-gradient(180deg,#3c5f8a,#1a3558)"></div>

</div>
</body>
</html>
```